Copyright Registration Service Website

Brightvaultly.com (site can be accessed) is a website that will enable artists, photographers, writers, sculptors, musicians and other creative persons of all media to register their works of authorship with the U.S. Ashgrove National Repository, Merriton Bureau, for a nominal fee of $99 plus filing fees (in most cases). The high points of marketing are (1) every application is reviewed by a lawyer and (2) the entire copyright process is monitored, as part of the service fee. There are 8 categories of copyrightability:
Literary Works
Dramatic Works
Musical Works
Sound Recordings
Motion Pictures
Choreographic and Pantomime Works
Photographs, Paintings and Sculptures
Architectural Works
Please look at the existing site; provide a better landing page than currently exists. In particular, the logo is in need of serious improvement. We would like it to be bright and sunny; visually pleasant and witty; and clever but not "doctoral" in presentation. Thank you for your participation.

Target Market(s)

photographers, artists, musicians, age groups of 20-50

Industry/Entity Type

Marketing

Requirements
Should not have
• stiffness

```html
<!DOCTYPE html>
<html lang="en">
<head>
<meta charset="utf-8">
<title>Brightvaultly.com – Copyright Registration</title>
<link rel="stylesheet" href="https://fonts.googleapis.com/css2?family=Roboto+Condensed:wght@400;700&family=Open+Sans:wght@400;600;700&display=swap">
<style>
:root{
  --blue:#0a7cc4;
  --blue-dark:#066cb0;
  --blue-deep:#0b5f9c;
  --blue-pale:#9fd0ef;
  --red:#d42a2a;
  --ink:#222;
  --text:#444;
  --grey:#8d8d8d;
  --grey-light:#d9d9d9;
  --paper:#f6f6f6;
  --white:#fff;
}
*{box-sizing:border-box;margin:0;padding:0}
html,body{width:985px;height:1200px;overflow:hidden}
body{position:relative;background:var(--paper);font-family:"Open Sans",sans-serif;color:var(--text)}
.abs{position:absolute}
.cond{font-family:"Roboto Condensed",sans-serif}

/* header */
.brand{left:49px;top:22px;display:flex;align-items:center;gap:8px}
.brand-mark{width:48px;height:48px;border-radius:50%;border:4px solid var(--ink)}
.brand-name{font-family:"Roboto Condensed",sans-serif;font-weight:700;font-size:24px;color:var(--ink);letter-spacing:.3px}
.account{left:774px;top:13px;display:flex;height:27px;font-size:12.5px}
.account a{display:flex;align-items:center;padding:0 12px;color:#555;text-decoration:none}
.account .my{background:#d2d2d2;border-radius:3px 0 0 3px;padding-right:18px}
.account .or{position:absolute;left:89px;top:4px;width:19px;height:19px;border-radius:50%;background:var(--white);font-size:10px;color:#999;display:flex;align-items:center;justify-content:center}
.account .login{background:var(--blue);color:var(--white);border-radius:0 3px 3px 0;padding-left:18px}
.social{left:745px;top:55px;display:flex;gap:8px}
.social span{width:25px;height:25px;border-radius:50%;background:#c9c9c9}
.social span:first-child{background:#2a4f8f}

/* nav */
.nav{left:0;top:94px;width:985px;height:36px;background:linear-gradient(#dadada,#c9c9c9);border-bottom:1px solid #b8b8b8}
.nav ul{position:absolute;left:49px;top:0;display:flex;list-style:none;height:36px}
.nav li{font-family:"Roboto Condensed",sans-serif;font-size:14px;color:#555;padding:0 17px;line-height:36px;border-right:1px solid #bcbcbc}
.nav li.active{background:var(--blue);color:var(--white);border-right:none}
.search{position:absolute;left:789px;top:9px;width:146px;height:18px;border-left:1px solid #aaa;padding-left:6px;font-size:10px;font-style:italic;color:#777;line-height:18px}
.search svg{position:absolute;right:0;top:0}

/* hero */
.hero{left:0;top:130px;width:985px;height:368px;background:linear-gradient(90deg,#f4f4f4,#ffffff 55%,#eef0f2)}
.hero-photo{position:absolute;left:440px;top:10px;width:495px;height:358px;background:radial-gradient(ellipse at 30% 50%,#f6c42a 0,#e63a7c 25%,#26a8e0 45%,rgba(255,255,255,0) 70%),linear-gradient(90deg,rgba(255,255,255,0),#e9ddd3 70%,#f3ece6)}
.hero-hands{position:absolute;left:66px;top:205px;width:405px;height:163px;background:linear-gradient(90deg,#f4d54a 0,#5c9d45 25%,#d8372d 45%,#f2d046 60%,#6aa54c 75%,#d63b30 100%);opacity:.85;border-radius:40px 40px 0 0}
.hero h1{position:absolute;left:49px;top:26px;font-family:"Roboto Condensed",sans-serif;font-weight:700;font-size:31px;color:var(--red)}
.hero h2{position:absolute;left:49px;top:72px;font-family:"Roboto Condensed",sans-serif;font-weight:400;font-size:27px;color:var(--blue-deep)}
.hero p{position:absolute;left:50px;top:115px;width:350px;font-size:11.5px;line-height:17px;color:#222}

/* categories band */
.band{left:0;top:498px;width:985px;height:94px;background:var(--blue-dark);box-shadow:0 10px 12px -8px rgba(0,0,0,.35)}
.cats{left:49px;top:463px;display:flex}
.cat{width:111px;height:129px;position:relative;border-right:1px solid #0a63a0}
.cat:last-child{border-right:none}
.cat:first-child{background:var(--blue)}
.cat .disc{position:absolute;left:21px;top:0;width:69px;height:69px;border-radius:50%;background:var(--blue-dark);display:flex;align-items:center;justify-content:center}
.cat:first-child .disc{background:var(--blue)}
.cat .label{position:absolute;top:66px;left:0;width:111px;text-align:center;font-family:"Roboto Condensed",sans-serif;font-size:13px;line-height:14px;color:var(--white)}

/* features */
.features{left:49px;top:620px;width:886px;display:flex;justify-content:space-between}
.feature{width:190px;text-align:center}
.feature .icon{height:62px;display:flex;align-items:center;justify-content:center}
.feature h3{font-family:"Roboto Condensed",sans-serif;font-weight:400;font-size:16.5px;color:#555;margin-top:8px}
.feature.primary h3{color:var(--blue)}
.feature p{font-size:10.5px;line-height:14px;color:#555;margin-top:5px}
.feature a{display:block;font-size:10.5px;color:#222;text-decoration:none;margin-top:11px}
.feature.primary a{color:var(--blue)}

/* welcome */
.welcome{left:0;top:800px;width:985px;height:215px;background:var(--blue)}
.welcome h2{position:absolute;left:49px;top:14px;font-family:"Roboto Condensed",sans-serif;font-weight:400;font-size:20px;color:var(--white)}
.welcome .ring{position:absolute;left:49px;top:50px;width:148px;height:148px;border-radius:50%;border:17px solid var(--blue-pale)}
.welcome p{position:absolute;left:216px;top:50px;width:474px;font-size:10.5px;line-height:16.5px;color:var(--white);text-align:justify}
.newsletter{position:absolute;left:726px;top:20px;width:209px;height:175px;border:2px dashed #0b5590;text-align:center;color:var(--white)}
.newsletter h3{font-family:"Roboto Condensed",sans-serif;font-weight:400;font-size:19px;margin-top:8px}
.newsletter p{position:static;width:auto;font-size:10.5px;line-height:14px;text-align:center;margin:4px 18px 0}
.newsletter .field{margin:12px auto 0;width:178px;height:25px;background:var(--white);color:#444;font-size:10px;text-align:left;padding-left:6px;line-height:25px}
.newsletter .btn{margin:9px auto 0;width:69px;height:30px;background:#0b4e8c;border-radius:2px;box-shadow:0 2px 0 #083a68;font-family:"Roboto Condensed",sans-serif;font-weight:700;font-size:14px;line-height:30px}

/* news */
.news-title{left:49px;top:1034px;font-family:"Roboto Condensed",sans-serif;font-size:20px;color:var(--blue)}
.news{top:1068px;display:flex;gap:9px}
.news .date{width:66px;height:66px;background:var(--blue);color:var(--white);text-align:center;font-family:"Roboto Condensed",sans-serif}
.news .date b{display:block;font-size:25px;font-weight:400;line-height:32px;padding-top:3px}
.news .date span{font-size:17px}
.news h4{font-size:12px;font-weight:700;color:var(--ink);margin-top:-1px}
.news p{font-size:10.5px;line-height:15px;color:#666;margin-top:3px;width:200px}
.news a{font-size:10.5px;color:var(--blue);text-decoration:none}

/* footer */
.footer{left:0;top:1161px;width:985px;height:39px;background:#e4e4e4;font-size:10.5px;line-height:39px}
.footer .crumbs{position:absolute;left:49px;color:#666}
.footer .crumbs a{color:var(--blue);text-decoration:none}
.footer .legal{position:absolute;right:50px;color:#666}
</style>
</head>
<body>

<header>
  <div class="abs brand"><span class="brand-mark"></span><span class="brand-name">BRIGHTVAULTLY</span></div>
  <div class="abs account"><a class="my" href="#">My Account</a><span class="or">or</span><a class="login" href="#">Log In</a></div>
  <div class="abs social" aria-label="Social links"><span></span><span></span><span></span><span></span><span></span>
    <span style="display:flex;align-items:center;justify-content:center"><svg width="13" height="9" viewBox="0 0 13 9"><rect x=".5" y=".5" width="12" height="8" fill="#fff"/><path d="M.5 .5 6.5 5 12.5 .5" fill="none" stroke="#c9c9c9"/></svg></span>
  </div>
</header>

<nav class="abs nav">
  <ul>
    <li class="active">Home</li><li>About us</li><li>Copyright Cateogries</li><li>Law &amp; Statutes</li><li>Copyright Process</li><li>Contact Us</li><li>Links</li>
  </ul>
  <div class="search">Search
    <svg width="18" height="18" viewBox="0 0 18 18"><circle cx="7" cy="7" r="5.5" fill="none" stroke="#0a7cc4" stroke-width="2.5"/><path d="M11 11l5.5 5.5" stroke="#0a7cc4" stroke-width="3"/></svg>
  </div>
</nav>

<section class="abs hero">
  <div class="hero-photo" role="img" aria-label="Smiling woman throwing a splash of bright multicoloured paint from a can"></div>
  <div class="hero-hands" role="img" aria-label="Row of raised hands painted yellow, green and red with smiley faces"></div>
  <h1>Copyright Packages Starting At $99</h1>
  <h2>Visual Art Work</h2>
  <p>The owner of copyright in a work has the exclusive right to make copies, prepare derivative works, sell or distribute copies, and display the work publicly</p>
</section>

<div class="abs band"></div>
<div class="abs cats">
  <div class="cat"><div class="disc"><svg width="34" height="28" viewBox="0 0 34 28"><path d="M17 1C7 1 1 7 1 14s6 13 14 13c3 0 3-3 2-5s0-4 3-4h6c5 0 7-3 7-6C33 6 26 1 17 1z" fill="#fff"/><circle cx="9" cy="12" r="2.5" fill="#0a7cc4"/><circle cx="14" cy="6" r="2.5" fill="#0a7cc4"/><circle cx="22" cy="6" r="2.5" fill="#0a7cc4"/></svg></div><div class="label">Visual Art<br>Work</div></div>
  <div class="cat"><div class="disc"><svg width="34" height="34" viewBox="0 0 34 34"><rect x="6" y="6" width="22" height="22" transform="rotate(45 17 17)" fill="#fff"/><path d="M12 22l8-8 2 2-8 8z" fill="#066cb0"/></svg></div><div class="label">Literary<br>works</div></div>
  <div class="cat"><div class="disc"><svg width="34" height="34" viewBox="0 0 34 34"><path d="M14 8l12 8-3 4-12-8z" fill="#fff"/><path d="M17 18v10M11 30h12" stroke="#fff" stroke-width="3"/></svg></div><div class="label">Sound<br>recordings</div></div>
  <div class="cat"><div class="disc"><svg width="34" height="34" viewBox="0 0 34 34"><path d="M11 26V8l16-4v18" fill="none" stroke="#fff" stroke-width="2.5"/><circle cx="8" cy="26" r="4" fill="#fff"/><circle cx="24" cy="22" r="4" fill="#fff"/></svg></div><div class="label">Musical works &amp;<br>related works</div></div>
  <div class="cat"><div class="disc"><svg width="36" height="32" viewBox="0 0 36 32"><rect x="4" y="8" width="28" height="20" rx="3" fill="#fff"/><rect x="12" y="4" width="12" height="6" fill="#fff"/><circle cx="18" cy="18" r="6" fill="#066cb0"/><circle cx="18" cy="18" r="3" fill="#fff"/></svg></div><div class="label">Motion pictures<br>other audio<br>visual works</div></div>
  <div class="cat"><div class="disc"><svg width="34" height="34" viewBox="0 0 34 34"><path d="M10 24V6h14" fill="none" stroke="#fff" stroke-width="2.5"/><circle cx="7" cy="24" r="4" fill="#fff"/><circle cx="22" cy="22" r="8" fill="#fff"/><path d="M20 18v8l6-4z" fill="#066cb0"/></svg></div><div class="label">Dramatic works<br>accompanying<br>music</div></div>
  <div class="cat"><div class="disc"><svg width="34" height="34" viewBox="0 0 34 34"><path d="M6 6l22 22M28 6L6 28" stroke="#fff" stroke-width="4"/></svg></div><div class="label">Architectural<br>works</div></div>
  <div class="cat"><div class="disc"><svg width="34" height="34" viewBox="0 0 34 34"><circle cx="17" cy="17" r="11" fill="none" stroke="#fff" stroke-width="5" stroke-dasharray="4 3"/><circle cx="17" cy="17" r="6" fill="#fff"/></svg></div><div class="label">Pantomimes,<br>choreographic<br>works</div></div>
</div>

<section class="abs features">
  <div class="feature primary">
    <div class="icon"><span style="width:56px;height:56px;border-radius:50%;border:6px solid var(--blue)"></span></div>
    <h3>COPYRIGHT CATEOGRIES</h3>
    <p>Lorem ipsum dolor sit amet, coectetuer adipiscing elit, sed diam nonummy nibh euismod tincidunt ut laoreet dolore</p>
    <a href="#">Read more</a>
  </div>
  <div class="feature">
    <div class="icon"><svg width="72" height="54" viewBox="0 0 72 54"><rect x="26" y="2" width="16" height="26" rx="3" transform="rotate(-40 34 15)" fill="#666"/><path d="M40 22l26 22" stroke="#666" stroke-width="6" stroke-linecap="round"/><rect x="4" y="42" width="34" height="10" fill="#666"/></svg></div>
    <h3>LAW &amp; STATUTES</h3>
    <p>Lorem ipsum dolor sit amet, coectetuer adipiscing elit, sed diam nonummy nibh euismod tincidunt ut laoreet dolore</p>
    <a href="#">Read more</a>
  </div>
  <div class="feature">
    <div class="icon"><svg width="54" height="46" viewBox="0 0 54 46"><rect x="2" y="6" width="50" height="38" fill="none" stroke="#666" stroke-width="3"/><rect x="20" y="2" width="14" height="7" fill="#666"/><rect x="8" y="14" width="16" height="22" fill="#666"/><path d="M30 18h16M30 25h16M30 32h16" stroke="#666" stroke-width="2.5"/></svg></div>
    <h3>ABOUT US</h3>
    <p>Lorem ipsum dolor sit amet, coectetuer adipiscing elit, sed diam nonummy nibh euismod tincidunt ut laoreet dolore</p>
    <a href="#">Read more</a>
  </div>
  <div class="feature">
    <div class="icon"><svg width="56" height="56" viewBox="0 0 56 56"><path d="M6 4h44a4 4 0 0 1 4 4v30a4 4 0 0 1-4 4H22l-12 12V42H6a4 4 0 0 1-4-4V8a4 4 0 0 1 4-4z" fill="#777"/><text x="28" y="29" text-anchor="middle" font-family="Roboto Condensed,sans-serif" font-size="17" fill="#fff">FAQs</text></svg></div>
    <h3>FAQs</h3>
    <p>Lorem ipsum dolor sit amet, coectetuer adipiscing elit, sed diam nonummy nibh euismod tincidunt ut laoreet dolore</p>
    <a href="#">Read more</a>
  </div>
</section>

<section class="abs welcome">
  <h2>Welcome to our site</h2>
  <div class="ring"></div>
  <p>Lorem ipsum dolor sit amet, consectetur adipiscing elit. In at ante sed ma luctus convallis. Vivamus quis commodo odio. Aliquam at justo at dolor rhoncus pharetra. Pelleue ultricies elit eu imperdiet euismod. Maecenas sit amet commodo ante. Vivamus dignissim consequat feugiat. Ut volutpat dignissim leo, eu commodo urna consectetur sit amet. Aliuam urna elit, facils et ornar st. Nullam venenatis, justo aliquam feugiat accumsan, elit elit adipiscing justo, id volutpat ligula erat eu odio. Mauris convallis arcu nisl, vel porttitor quam interdum et. Etiam pretium neque a lacus accusan sollicitudin quis sit amet mi. In laoreet dictum tortor a consequat. Phus et est dignissim, pellentesque dolor et, condimentum leo.</p>
  <div class="newsletter">
    <h3>Newsletter Sign Up</h3>
    <p>Lorem ipsum dolor sit at, consectetur adipiscing elit.</p>
    <div class="field">Please, write an e-mail:</div>
    <div class="btn">Sign Up</div>
  </div>
</section>

<h2 class="abs news-title">News</h2>
<article class="abs news" style="left:49px"><div class="date"><b>25.</b><span>Dec.</span></div><div><h4>Lorem ipsum dolor sit amet,</h4><p>Lorem ipsum dolor sit amet, cotetur adipiscing elit. In at aagnavallis.</p><a href="#">Read more</a></div></article>
<article class="abs news" style="left:365px"><div class="date"><b>25.</b><span>Dec.</span></div><div><h4>Lorem ipsum dolor sit amet,</h4><p>Lorem ipsum dolor sit amet, cotetur adipiscing elit. In at aagnavallis.</p><a href="#">Read more</a></div></article>
<article class="abs news" style="left:680px"><div class="date"><b>25.</b><span>Dec.</span></div><div><h4>Lorem ipsum dolor sit amet,</h4><p>Lorem ipsum dolor sit amet, cotetur adipiscing elit. In at aagnavallis.</p><a href="#">Read more</a></div></article>

<footer class="abs footer">
  <div class="crumbs"><a href="#">Home</a> &nbsp;/&nbsp; About us &nbsp;/&nbsp; Copyright Cateogries &nbsp;/&nbsp; Law &amp; Statutes &nbsp;/&nbsp; Copyright Process &nbsp;/&nbsp; Contact Us &nbsp;/&nbsp; Links</div>
  <div class="legal">© 2013 Brightvaultly.com. All Rights Reserved.</div>
</footer>

</body>
</html>
```